Harbor Sushi & Steak Dinner Menu

I'm looking for a MENU design with a particular feel. I want to have a base template made that I can then use for future alterations to the menu; ie I can go in and change out different entrees as the menu changes but the template will remain the same. (Ideally it would be in an Apple Pages format.). Also ideally - dinner menu will occupy 2 pages 8.5 x 11. The restaurant's name is Harbor. It is a MODERN steak house that will also feature Sushi, a Raw Bar, Exquisite Cocktails and a sophisticated nightlife crowd. I have attached our LOGO, a secondary logo that we will be featuring throughout the project including on the menu cover (the gold U). Finally - I have attached the content that we would like to see. AGAIN - I REITERATE: High end dining and lounge atmosphere. A couple of restaurants / menus that I love are Morvendel in NYC and Pellucid Steakhouse in Long Island NY. Please do not duplicate - just trying to offer some suggestions.

Requirements
Must have
• A sophisticated and elegant feel without being stuffy or old.

```html
<!DOCTYPE html>
<html lang="en">
<head>
<meta charset="utf-8">
<title>Harbor Sushi &amp; Steak – Dinner Menu</title>
<link href="https://fonts.googleapis.com/css2?family=Josefin+Sans:wght@400;600;700&display=swap" rel="stylesheet">
<style>
:root{
  --backdrop:#6a6a6a;
  --panel:#0c0c0c;
  --band:#d3233e;
  --heading:#e8344e;
  --gold:#e3c98b;
  --ink:#e9e9e9;
}
*{box-sizing:border-box;margin:0;padding:0}
html,body{width:1200px;height:2227px;overflow:hidden}
body{background:var(--backdrop);font-family:"Josefin Sans",sans-serif;color:var(--ink)}
.spread{display:grid;grid-template-columns:560px 560px;grid-template-rows:repeat(3,717px);column-gap:24px;row-gap:18px;padding:20px 28px}
.panel{position:relative;background:var(--panel);overflow:hidden;padding:60px 40px 36px 48px}
.panel::before,.panel::after{content:"";position:absolute;left:0;right:0;height:24px;background:var(--band)}
.panel::before{top:0}
.panel::after{bottom:0}
.ribbon{position:absolute;top:0;right:44px;width:64px;height:90px}
.panel.spaced{padding-top:100px}
.section-title{font-weight:700;font-size:20px;line-height:24px;letter-spacing:4px;color:var(--heading);margin:12px 0 4px;display:flex;justify-content:space-between;max-width:380px}
.section-title:first-of-type{margin-top:0}
.section-title.full{max-width:none;padding-right:0}
.item{display:grid;grid-template-columns:118px 1fr 34px;font-size:12.5px;line-height:1.32;margin-bottom:1px}
.item .name{color:var(--gold);font-weight:600}
.item .desc{color:var(--ink)}
.item .desc:last-child{grid-column:2/4}
.item .gf{color:var(--gold);text-align:right}
.item.wide{grid-template-columns:auto 1fr 34px}
.item.wide .name{padding-right:6px}
.pair{display:grid;grid-template-columns:1fr 1fr;column-gap:18px}
.pair .item{grid-template-columns:62px 1fr 32px}
.line{font-size:12.5px;line-height:1.4;margin-bottom:3px;padding-left:90px;text-indent:-90px}
.line .name{color:var(--gold);font-weight:600}
.line .indent{display:block;text-indent:0}
.gap{margin-bottom:10px}
.cover{display:flex;align-items:center;justify-content:center;padding:0}
.wordmark{font-weight:700;color:var(--gold);letter-spacing:10px;font-size:96px;line-height:1;display:flex;align-items:center;gap:18px}
.wordmark .dot{width:22px;height:22px;border-radius:50%;background:var(--heading)}
.back{display:flex;align-items:flex-end;justify-content:flex-end;padding:0 60px 110px 0}
.back .wordmark{font-size:44px;letter-spacing:5px;gap:10px}
.back .wordmark .dot{width:11px;height:11px}
</style>
</head>
<body>
<svg width="0" height="0" style="position:absolute" aria-hidden="true">
  <defs>
    <linearGradient id="ribbonFill" x1="0" y1="0" x2="0" y2="1">
      <stop offset="0" stop-color="#e9cf94"/>
      <stop offset="1" stop-color="#c77a5a"/>
    </linearGradient>
  </defs>
</svg>
<main class="spread">

  <section class="panel cover">
    <div class="wordmark"><span class="dot"></span>Harbor</div>
  </section>

  <section class="panel">
    <svg class="ribbon" viewBox="0 0 64 90"><path d="M0 0H64V90L32 77L0 90Z" fill="url(#ribbonFill)"/></svg>
    <h2 class="section-title">SUSHI / SASHIMI</h2>
    <div class="pair">
      <div>
        <div class="item"><span class="name">Toro;</span><span class="desc">blue fin tuna belly</span><span class="gf">(gf)</span></div>
        <div class="item"><span class="name">Ebi;</span><span class="desc">cooked shrimp</span><span class="gf">(gf)</span></div>
        <div class="item"><span class="name">Hamachi;</span><span class="desc">yellowtail</span><span class="gf">(gf)</span></div>
        <div class="item"><span class="name">Uni;</span><span class="desc">sea urchin</span><span class="gf">(gf)</span></div>
        <div class="item"><span class="name">Hirame;</span><span class="desc">fluke</span><span class="gf">(gf)</span></div>
      </div>
      <div>
        <div class="item"><span class="name">&nbsp;</span><span class="desc"></span></div>
        <div class="item"><span class="name">Unagi;</span><span class="desc">fresh water eel</span><span class="gf">(gf)</span></div>
        <div class="item"><span class="name">Sake;</span><span class="desc">salmon</span><span class="gf">(gf)</span></div>
        <div class="item"><span class="name">Madai;</span><span class="desc">red snapper</span><span class="gf">(gf)</span></div>
        <div class="item"><span class="name">Maguro;</span><span class="desc">tuna</span><span class="gf">(gf)</span></div>
      </div>
    </div>
    <h2 class="section-title">SUSHI PLATTERS</h2>
    <div class="item"><span class="name">Small:</span><span class="desc">Five Pieces assorted sushi, nine pieces sashimi, spicy tuna roll</span><span class="gf">(gf)</span></div>
    <div class="item"><span class="name">Large:</span><span class="desc">Eight Pieces assorted sushi, eighteen pieces of sashimi, alaskan roll, rainbow roll</span><span class="gf">(gf)</span></div>
    <h2 class="section-title">CLASSIC ROLLS</h2>
    <div class="item"><span class="name">Yellowtail;</span><span class="desc">inside out roll with scallions</span><span class="gf">(gf)</span></div>
    <div class="item wide"><span class="name">Spicy Tuna or Salmon or Yellowtail;</span><span class="desc">spicy mayo</span></div>
    <div class="item"><span class="name">California:</span><span class="desc">crab meat, cucumber and avocado</span><span class="gf">(gf)</span></div>
    <div class="item"><span class="name">Vegetable:</span><span class="desc">avocado, cucumber, asparagus and pickled reddish</span><span class="gf">(gf)</span></div>
    <div class="item"><span class="name">Spider:</span><span class="desc">soft shell crab and avocado with eel sauce</span></div>
    <div class="item"><span class="name">Shrimp Tempura:</span><span class="desc">deep fried tempura shrimp and eel sauce</span></div>
    <div class="item"><span class="name">Alaskan;</span><span class="desc">salmon and avocado</span><span class="gf">(gf)</span></div>
    <h2 class="section-title">SPECIAL ROLLS</h2>
    <div class="item"><span class="name">The Harbor:</span><span class="desc">tuna, salmon, yellowtail, avocado, spicy mayo, soy bean paper</span></div>
    <div class="item"><span class="name">King Crab Rainbow:</span><span class="desc">king crab, avocado, cucumbers, assorted fish on top</span></div>
    <div class="item"><span class="name">Empress:</span><span class="desc">Shrimp tempura, spicy tuna on top, eel sauce, spicy mayo</span></div>
    <div class="item"><span class="name">Spicy Girl:</span><span class="desc">Spicy crunchy crab meat, cucumber, shrimp on top</span></div>
    <div class="item"><span class="name">Dragon:</span><span class="desc">Eel, cucumber, avocado, and tobiko on top, eel sauce</span></div>
    <div class="item"><span class="name">Yummy:</span><span class="desc">spicy crunchy salmon, avocado, mango and salmon on top</span></div>
    <div class="item"><span class="name">No. 9:</span><span class="desc">Shrimp Tempura, avocado, kani, spicy mayo, tobiko</span></div>
    <div class="item"><span class="name">Sunrise Roll:</span><span class="desc">spicy crunchy tuna and avocado, spicy crunchy salmon on top</span></div>
  </section>

  <section class="panel spaced">
    <svg class="ribbon" viewBox="0 0 64 90"><path d="M0 0H64V90L32 77L0 90Z" fill="url(#ribbonFill)"/></svg>
    <h2 class="section-title">SEAFOOD RAW BAR</h2>
    <p class="line"><span class="name">Lobster Cocktail</span></p>
    <p class="line"><span class="name">Shrimp Cocktail</span></p>
    <p class="line"><span class="name">Clams on the Half Shell</span></p>
    <p class="line"><span class="name">Oysters on the Half Shell</span></p>
    <p class="line gap"><span class="name">Colossal Crab Cocktail</span></p>
    <p class="line"><span class="name">Raw Bar Plate for One:</span><span class="indent">Two Shrimp, Half of a One Pound Lobster,<br>Two Clams, One East Coast Oyster, One West Coast Oyster</span></p>
    <h2 class="section-title full"><span>SEAFOOD PLATTERS</span><span>(gf)</span></h2>
    <p class="line"><span class="indent">Shrimp, Oysters, Clams, Lobster and Crab</span></p>
    <p class="line"><span class="name">Large or Colossal</span></p>
    <h2 class="section-title">APPS</h2>
    <p class="line"><span class="name">BAO Bun;</span> hoisin bbq pancetta cut pork loin, crispy onions, micro mint</p>
    <p class="line"><span class="name">Five Spice Crispy Popcorn Crusted Prawns (2);</span> classic burre blanc</p>
    <p class="line"><span class="name">Jumbo Lump Crab;</span> citrus miso drizzle, spring pea puree, micro greens</p>
    <p class="line"><span class="name">Crispy Wonton Napoleon;</span> cucumber gallete, ahi tuna, jumbo lump crab meat, wasabi aioli, shoestring wontons</p>
    <p class="line"><span class="name">PEI Mussels;</span> charred artichoke hearts, blistered heirloom tomatoes, garlic white wine broth</p>
    <p class="line"><span class="name">New Zealand or Domestic Small Eye Lamb Chop (1);</span> crispy porcini risotto cake</p>
  </section>

  <section class="panel spaced">
    <svg class="ribbon" viewBox="0 0 64 90"><path d="M0 0H64V90L32 77L0 90Z" fill="url(#ribbonFill)"/></svg>
    <h2 class="section-title">SALADS</h2>
    <div class="item"><span class="name">Classic Wedge;</span><span class="desc">bleu cheese, bacon lardons, heirloom tomatoes</span></div>
    <p class="line"><span class="name">Mixed Baby Greens;</span> heirloom tomatoes, cucumber, red onion, dijon vinaigrette</p>
    <div class="item gap"><span class="name">Tabulleh;</span><span class="desc">buckwheat grain, fresh mint, tomato concasse, cucumber, parsley, fresh squeezed lemon, EVOO, salt and pepper</span></div>
    <p class="line"><span class="name">Tomato Mozzarella Salad / Burratta</span></p>
    <div class="item"><span class="name">Spinach Salad;</span><span class="desc">green apple, feta, currants, with per-simmons vinaigrette</span></div>
    <div class="item"><span class="name">Kale Caesar;</span><span class="desc">homemade cacio e'peppe dressing, pecorino and parmesan cheese, toasted croutons.</span></div>
    <h2 class="section-title">ENTREES</h2>
    <p class="line"><span class="name">Pan Roasted Miso Glazed Black Cod;</span> green tea noodle stir fry; Napa cabbage, carrot, Japanese eggplant</p>
    <p class="line"><span class="name">Pan Seared Striped Bass;</span> lobster succotash in a tomato saffron broth</p>
    <p class="line"><span class="name">E.V.O.O. Salted / Grilled Swordfish;</span> sun dried tomato, olive and caper tapenade, over basmati rice</p>
    <p class="line"><span class="name">Grilled Half Chicken;</span> sun dried tomato and basil Israeli cous-cous, pan au jus</p>
    <p class="line"><span class="name">Roasted Fresh Caviatelle Ratatoille;</span> vegetable broth</p>
    <p class="line"><span class="name">Lobster Cartoccio;</span> shrimp, mussels, clams, fresh herb tomato broth, tossed with bucatini, charred artichoke hearts, heirloom tomatoes, caper berries, spring onions, fresh basil, white wine reduction over forbidden rice (gf)</p>
    <p class="line"><span class="name">Mediterranean Grilled Veggie Plate;</span> artichoke hearts, Japanese eggplant, green &amp; white asparagus, seared heirloom tomatoes, roasted baby carrots, cauliflower rice, evoo &amp; fig drizzle (gf)</p>
  </section>

  <section class="panel spaced">
    <svg class="ribbon" viewBox="0 0 64 90"><path d="M0 0H64V90L32 77L0 90Z" fill="url(#ribbonFill)"/></svg>
    <h2 class="section-title"><span>USDA PRIME STEAKS &nbsp;&nbsp;(gf)</span></h2>
    <p class="line"><span class="name">10 Oz Filet</span></p>
    <p class="line"><span class="name">14 or 16 oz New York Strip</span></p>
    <p class="line"><span class="name">24 oz Boneless Ribeye</span></p>
    <p class="line"><span class="name">36 oz Bone in Rib Eye</span></p>
    <p class="line"><span class="name">Berkshire Pork Chop</span></p>
    <h2 class="section-title">SAUCES</h2>
    <p class="line"><span class="name">Cabernet Demi Glaz</span></p>
    <p class="line"><span class="name">Gorganzola Brulle Cream</span></p>
    <p class="line"><span class="name">Truffled Wild Mushroom Ragu</span></p>
    <p class="line"><span class="name">Horseradish Cream</span></p>
    <p class="line"><span class="name">House Steak Sauce</span></p>
    <h2 class="section-title">SIDES</h2>
    <p class="line"><span class="name">Mashed Idaho Potatoes</span></p>
    <p class="line"><span class="name">Bacon, Sweet Corn, Caramelized Vidalia Onion fingerling potatoes</span></p>
    <p class="line"><span class="name">Roasted Peanut Potatoes</span></p>
    <p class="line"><span class="name">Creamed Spinach</span></p>
    <p class="line"><span class="name">Sautéed Spinach</span></p>
    <p class="line"><span class="name">Grilled Asparagus</span></p>
    <p class="line"><span class="name">French Beans</span></p>
    <p class="line"><span class="name">Israeli Cous Cous</span></p>
    <p class="line"><span class="name">Sweet Potato Steak Fries</span></p>
    <p class="line"><span class="name">Corn Skillet</span></p>
  </section>

  <section class="panel back">
    <div class="wordmark"><span class="dot"></span>Harbor</div>
  </section>

</main>
</body>
</html>
```